T.R.L (Tidal Resonance Lifting) is a form of energy healing that raises the vibration of the DNA so that it releases old energy patterns that no longer serve you. This allows the body to remember its natural ability to heal itself perfectly.

The energy is called in telepathically from the Acturians, the dolphins, the platinum ray and the Octahedron.

I would like a logo that incorporates all of these moadlities.

I will also require help with setting up my facebook page and website but until these are setup I cannot include the details so space will need to be saved for this on the business card

Target Market(s)

Alternative health

Industry/Entity Type

Business

Logo Text

T.R.L

Requirements
Must have
• Colors of the platinum ray. I have drafted the below as to what I would like it to say on it:-

Business Card –
Front:-
Lifting You To A Brighter Frequency
Mabel Thornby
Tidal Resonance Lifting Facilitator
www.quorvintel.example
+(61) 412 735 289 mabelthornby4471@quorvintel.example

Back:-
Appointments
For:-
Date: Time:
Location:

```html
<!DOCTYPE html>
<html lang="en">
<head>
<meta charset="utf-8">
<title>T.R.L Business Card</title>
<link rel="stylesheet" href="https://fonts.googleapis.com/css2?family=Archivo+Black&family=Archivo:wght@800&family=Quicksand:wght@400;500&display=swap">
<style>
  :root {
    --blue-deep: #2a2f9c;
    --blue-mid: #2348b0;
    --blue-bright: #1a7bd0;
    --orange: #f26a1f;
    --orange-light: #f7951f;
    --white: #ffffff;
    --page: #eef0f3;
    --ink-blue: #22349d;
  }
  * { box-sizing: border-box; margin: 0; padding: 0; }
  html, body { width: 1200px; height: 900px; overflow: hidden; }
  body { background: var(--page); position: relative; font-family: "Quicksand", sans-serif; }

  .card {
    position: absolute;
    width: 540px;
    height: 310px;
    box-shadow: 0 10px 24px rgba(0,0,0,0.18);
  }
  .card--front { left: 40px; top: 295px; }
  .card--back { left: 620px; top: 295px; }
  .card__frame { position: absolute; inset: 0; width: 100%; height: 100%; display: block; }

  /* Front */
  .brand-name {
    position: absolute; left: 0; right: 0; top: 78px;
    text-align: center;
    font-family: "Archivo Black", sans-serif;
    font-size: 78px; letter-spacing: 2px;
    color: var(--blue-mid);
    line-height: 1;
  }
  .tagline {
    position: absolute; left: 0; right: 0; top: 170px;
    text-align: center;
    font-family: "Archivo", sans-serif; font-weight: 800;
    font-size: 20px; color: var(--ink-blue);
  }
  .web-links { position: absolute; left: 62px; top: 214px; list-style: none; }
  .web-links li {
    display: flex; align-items: center; gap: 12px;
    font-family: "Archivo", sans-serif; font-weight: 800;
    font-size: 14px; color: var(--orange); letter-spacing: 0.5px;
    height: 30px;
  }
  .web-links .dot {
    width: 20px; height: 20px; border-radius: 50%;
    background: var(--ink-blue); flex: none;
  }

  /* Back */
  .holder-name {
    position: absolute; left: 0; right: 0; top: 30px;
    text-align: center;
    font-family: "Archivo", sans-serif; font-weight: 800;
    font-size: 22px; color: var(--ink-blue); letter-spacing: 0.5px;
  }
  .holder-role {
    position: absolute; left: 0; right: 0; top: 58px;
    text-align: center;
    font-size: 19px; font-weight: 500; color: var(--orange);
  }
  .contact { position: absolute; right: 40px; top: 112px; list-style: none; text-align: right; }
  .contact li {
    display: flex; justify-content: flex-end; align-items: center; gap: 8px;
    font-size: 14px; font-weight: 500; color: var(--ink-blue); height: 28px;
  }
  .contact svg { width: 20px; height: 16px; flex: none; }
  .appointments { position: absolute; left: 48px; top: 150px; }
  .appointments__title {
    font-family: "Archivo", sans-serif; font-weight: 800;
    font-size: 16px; color: var(--ink-blue); letter-spacing: 0.5px;
  }
  .appointments__fields { list-style: none; }
  .appointments__fields li { font-size: 17px; color: var(--orange); line-height: 25px; }
</style>
</head>
<body>

<section class="card card--front" aria-label="Business card front">
  <svg class="card__frame" viewBox="0 0 540 310" preserveAspectRatio="none" aria-hidden="true">
    <defs>
      <linearGradient id="blueFront" x1="0" y1="1" x2="1" y2="0">
        <stop offset="0" stop-color="#2a2f9c"/>
        <stop offset="1" stop-color="#1a7bd0"/>
      </linearGradient>
      <linearGradient id="orangeFront" x1="0" y1="0" x2="1" y2="0">
        <stop offset="0" stop-color="#f26a1f"/>
        <stop offset="1" stop-color="#f7951f"/>
      </linearGradient>
    </defs>
    <rect width="540" height="310" fill="url(#blueFront)"/>
    <polygon points="0,0 210,0 180,24 34,24 34,200 0,240" fill="url(#orangeFront)"/>
    <polygon points="540,70 540,310 300,310 332,286 508,286 508,100" fill="url(#orangeFront)"/>
    <polygon points="34,24 508,24 508,286 34,286" fill="#ffffff"/>
  </svg>
  <h1 class="brand-name">T.R.L</h1>
  <p class="tagline">Lifting You To A Brighter Frequency</p>
  <ul class="web-links">
    <li><span class="dot"></span>WWW.FRIENDSPACE.EXAMPLE/TRL</li>
    <li><span class="dot"></span>WWW.QUORVINTEL.EXAMPLE</li>
  </ul>
</section>

<section class="card card--back" aria-label="Business card back">
  <svg class="card__frame" viewBox="0 0 540 310" preserveAspectRatio="none" aria-hidden="true">
    <defs>
      <linearGradient id="blueBack" x1="0" y1="1" x2="1" y2="0">
        <stop offset="0" stop-color="#2a2f9c"/>
        <stop offset="1" stop-color="#1a7bd0"/>
      </linearGradient>
      <linearGradient id="orangeBack" x1="0" y1="0" x2="1" y2="0">
        <stop offset="0" stop-color="#f26a1f"/>
        <stop offset="1" stop-color="#f7951f"/>
      </linearGradient>
    </defs>
    <rect width="540" height="310" fill="url(#blueBack)"/>
    <polygon points="0,0 200,0 172,22 30,22 30,220 0,250" fill="url(#orangeBack)"/>
    <polygon points="540,90 540,310 330,310 360,290 512,290 512,118" fill="url(#orangeBack)"/>
    <polygon points="30,22 512,22 512,290 30,290" fill="#ffffff"/>
  </svg>
  <h2 class="holder-name">MABEL THORNBY</h2>
  <p class="holder-role">Tidal Resonance Lifting Facilitator</p>
  <ul class="contact">
    <li>mabelthornby4471@quorvintel.example
      <svg viewBox="0 0 20 16" aria-hidden="true"><rect x="1" y="2" width="18" height="12" fill="#f26a1f"/><polyline points="1,2 10,9 19,2" fill="none" stroke="#ffffff" stroke-width="1.5"/></svg>
    </li>
    <li>+(61) 412 735 289
      <svg viewBox="0 0 20 16" aria-hidden="true"><path d="M6 1 L9 4 L7 6 Q9 10 13 12 L15 10 L18 13 L15 16 Q4 13 3 3 Z" fill="#f26a1f"/></svg>
    </li>
  </ul>
  <div class="appointments">
    <h3 class="appointments__title">APPOINTMENTS</h3>
    <ul class="appointments__fields">
      <li>For</li>
      <li>Date</li>
      <li>Time</li>
      <li>Location</li>
    </ul>
  </div>
</section>

</body>
</html>
```